Super Greens Label for Supplement Bottle

We want to design a front label for a health supplement bottle. The product is called Meadow Twist Chews™. This will be a new product so there is no current website for the product. The focus is on supergreens that taste great and deliver support for energy, digestion, and immune defense.
We want it to be modern, vibrant and appealing.
Bottle size: standard size supplement CLEAR bottle size, with white child resistant cap and the label panel dimensions are 3” x 7”. The label should be primarily white and green, with a touch of red; (see color palettes)/it can also ONLY be white and green. See samples attached.
We are only focused on the front of the bottle design, not on the back, but leave space for the supplement panel and other text on the back.
So the text for the front of the bottle is:
RT Balden's
Meadow Twist Chews™
Super Greens Blend for:
Energy, Digestion, and Immune Support*
60 Gummies | Dietary Supplement
Raspberry Flavor Gummies
Off to side of the label:
Non-GMO
Vegan Friendly
Plant-Based
Gelatin Free
Colors
Designer to choose colors to be used in the design.

```html
<!DOCTYPE html>
<html lang="en">
<head>
<meta charset="utf-8">
<title>Meadow Twist Chews – Front Label</title>
<link rel="stylesheet" href="https://fonts.googleapis.com/css2?family=Poppins:ital,wght@0,400;0,600;0,700;1,600&family=Montserrat:wght@300;400&display=swap">
<style>
  :root{
    --page:#e7e7e7;
    --white:#ffffff;
    --green-deep:#05523a;
    --green:#0b6b4b;
    --green-light:#13805a;
    --brand-green:#117a55;
    --mint:#27d08a;
    --mint-deep:#0fae6c;
    --red:#c8102e;
    --berry:#d63a57;
    --leaf:#79b23a;
    --ink:#ffffff;
  }
  *{margin:0;padding:0;box-sizing:border-box}
  html,body{width:744px;height:1200px;overflow:hidden;background:var(--page)}
  .label{
    position:absolute;left:22px;top:450px;width:700px;height:300px;
    background:radial-gradient(ellipse at 50% 45%,var(--green-light),var(--green) 45%,var(--green-deep));
    box-shadow:0 6px 14px rgba(0,0,0,.18);
    overflow:hidden;font-family:"Montserrat",sans-serif;color:var(--ink);
  }
  .band-top{position:absolute;left:0;top:0;width:100%;height:15px;background:var(--white)}
  .band-bottom{position:absolute;left:0;top:284px;width:100%;height:16px;background:var(--white)}
  .brand-tab{
    position:absolute;left:266px;top:0;width:167px;height:45px;background:var(--white);
    border-radius:0 0 10px 10px;display:flex;align-items:center;justify-content:center;
    font-family:"Poppins",sans-serif;font-weight:700;font-size:22px;color:var(--brand-green);letter-spacing:1px;
  }
  .title{position:absolute;left:0;width:100%;text-align:center;font-family:"Poppins",sans-serif}
  .title-main{top:58px;font-weight:700;font-size:29px;letter-spacing:-.3px}
  .title-sub{top:96px;font-family:"Montserrat",sans-serif;font-weight:300;font-size:17px;letter-spacing:21px;padding-left:21px}
  .rule{position:absolute;left:240px;top:124px;width:219px;height:1px;background:rgba(255,255,255,.5)}
  .blend{position:absolute;left:0;width:100%;top:131px;text-align:center;font-size:11.5px;letter-spacing:2.4px;font-weight:400}
  .benefit-pill{
    position:absolute;left:240px;top:155px;width:219px;height:18px;border-radius:9px;
    background:linear-gradient(90deg,var(--mint-deep),var(--mint));border:1px solid #b9f5d7;
    font-size:8.6px;display:flex;align-items:center;justify-content:center;
  }
  .claim{position:absolute;display:flex;align-items:center;gap:5px;font-size:12.5px;font-weight:400}
  .claim svg{width:18px;height:18px}
  .fruit{
    position:absolute;left:356px;top:198px;width:104px;height:86px;border-radius:45% 45% 40% 40%;
    background:radial-gradient(circle at 60% 65%,var(--berry),#a8153a 60%,transparent 72%),
               radial-gradient(circle at 55% 15%,var(--leaf),transparent 45%);
  }
  .flavor-stripe{
    position:absolute;left:270px;top:270px;width:196px;height:14px;background:var(--red);
    font-family:"Poppins",sans-serif;font-style:italic;font-weight:600;font-size:6.5px;padding:3px 0 0 5px;
  }
  .count-block{
    position:absolute;left:233px;top:268px;width:37px;height:32px;background:var(--red);
    text-align:center;font-family:"Poppins",sans-serif;line-height:1;
  }
  .count-block .num{display:block;font-weight:700;font-size:20px;margin-top:3px}
  .count-block .unit{display:block;font-size:5px}
  .supplement{position:absolute;left:273px;top:287px;font-size:6px;letter-spacing:1.6px;color:#222;font-weight:400}
</style>
</head>
<body>
<div class="label">
  <div class="band-top"></div>
  <div class="brand-tab">RT Balden's</div>

  <div class="title title-main">MEADOW TWIST</div>
  <div class="title title-sub">CHEWS</div>
  <div class="rule"></div>
  <div class="blend">SUPER GREENS BLEND FOR:</div>
  <div class="benefit-pill">Energy, Digestion, And Immune Support*</div>

  <div class="claim" style="left:240px;top:183px">
    <svg viewBox="0 0 18 18"><circle cx="9" cy="9" r="8" fill="none" stroke="#fff" stroke-width="1"/><path d="M7 4h4M8 4v4l-3 5h8l-3-5V4" fill="none" stroke="#fff" stroke-width="1"/></svg>Non-GMO
  </div>
  <div class="claim" style="left:340px;top:183px">
    <svg viewBox="0 0 18 18"><circle cx="9" cy="9" r="8" fill="none" stroke="#fff" stroke-width="1"/><path d="M5 13c1-5 4-7 8-8-1 4-3 7-8 8zM5 13l5-5" fill="none" stroke="#fff" stroke-width="1"/></svg>Vegan Friendly
  </div>
  <div class="claim" style="left:240px;top:210px">
    <svg viewBox="0 0 18 18"><circle cx="9" cy="9" r="8" fill="none" stroke="#fff" stroke-width="1"/><path d="M9 14V8M9 8c0-3-3-4-4-4 0 2 1 4 4 4zM9 9c0-3 3-4 4-4 0 2-1 4-4 4z" fill="none" stroke="#fff" stroke-width="1"/></svg>Plant-Based
  </div>
  <div class="claim" style="left:240px;top:237px">
    <svg viewBox="0 0 18 18"><circle cx="9" cy="9" r="8" fill="none" stroke="#fff" stroke-width="1"/><path d="M5 9a4 4 0 0 1 8 0zM9 9v5M7 14h4" fill="none" stroke="#fff" stroke-width="1"/></svg>Gelatin Free
  </div>

  <div class="fruit" role="img" aria-label="Raspberries with green leaves"></div>

  <div class="band-bottom"></div>
  <div class="flavor-stripe">Raspberry Flavor Gummies</div>
  <div class="count-block"><span class="num">60</span><span class="unit">Gummies</span></div>
  <div class="supplement">▸Dietary Supplement</div>
</div>
</body>
</html>
```